Flyer for annual KESTREL SUMMIT 2020

I would like a church event flyer designed. The event is called "KESTREL SUMMIT 2020". I am looking for a professional, yet catchy design that uses our brand colors and logo creatively while communicating key information of the event effectively.

1. The logo is attached in two color formats. The designer has the choice to use them as he/she want.

2. The location of the event is: Harlow Community Center, 239 Fennimore Street, Portland, ME 04117

3. Time and date of event. The designer can organize and format the date and time as he/she pleases.
Thursday December 31st @ 6:30PM
Friday January 1st @ 6:30PM
Saturday 2nd @ 6:30PM
Sunday 3rd @ 4:30PM

4. The topic of the event is "In Fire and On Fire". The designer is free to use this phrase as he/she pleases to create a good composition.

5. Speaker: Prophet Marcus Olunde (2 pictures of the speaker to choose from are attached)

6. Contact information: contact@brightmeadowfold.org - Telephone number: 207 583 2914

7. I would also like the following three words on the flyer. These words describe the focus of the event: FIRE, REVIVAL, PROPHETIC

Target Market(s)

Young adults

Font styles to use
Sans Serif

Requirements
Must have
• Logo, speaker's picture
Should not have
• cross image, church image

```html
<!DOCTYPE html>
<html lang="en">
<head>
<meta charset="utf-8">
<title>Kestrel Summit 2020 – Flyer</title>
<link rel="stylesheet" href="https://fonts.googleapis.com/css2?family=Jost:wght@100;200;300;400;500;600;700;800&display=swap">
<style>
  :root {
    --flame-red: #cf4a35;
    --flame-mid: #e4743c;
    --flame-yellow: #fde85a;
    --amber: #e0913a;
    --amber-deep: #d9822f;
    --royal: #23579c;
    --royal-light: #2f6fbf;
    --navy: #1f2a48;
    --navy-ink: #1d2c4f;
    --paper: #ffffff;
    --blush: #f7e4d8;
  }
  * { box-sizing: border-box; margin: 0; padding: 0; }
  html, body {
    width: 1200px; height: 1200px; overflow: hidden;
    background: var(--paper);
    font-family: "Jost", sans-serif;
  }
  .flyer {
    position: absolute; left: 200px; top: 81px;
    width: 807px; height: 1044px;
    background: var(--navy);
    box-shadow: 4px 6px 12px rgba(0,0,0,.35);
    overflow: hidden;
  }
  .panel { position: absolute; }
  .panel--flame {
    left: 0; top: 0; width: 358px; height: 1044px;
    background:
      radial-gradient(ellipse 60% 35% at 70% 55%, rgba(253,232,90,.75), rgba(253,232,90,0) 70%),
      linear-gradient(172deg, var(--flame-red) 0%, var(--flame-red) 30%, var(--flame-mid) 50%, #f5b84a 66%, var(--flame-yellow) 82%, var(--flame-yellow) 100%);
  }
  .panel--brand {
    left: 358px; top: 0; width: 351px; height: 211px;
    background: var(--paper);
    display: flex; align-items: center; justify-content: center; gap: 14px;
  }
  .brand-dot { width: 26px; height: 26px; border-radius: 50%; background: var(--amber); }
  .brand-name {
    font-weight: 500; font-size: 58px; letter-spacing: 2px;
    color: var(--navy-ink);
  }
  .panel--year { left: 709px; top: 0; width: 98px; height: 211px; background: var(--flame-red); }
  .panel--title {
    left: 358px; top: 211px; width: 449px; height: 218px;
    background: linear-gradient(160deg, var(--royal) 0%, var(--royal-light) 55%, var(--royal) 100%);
  }
  .panel--details {
    left: 358px; top: 429px; width: 449px; height: 615px;
    background: linear-gradient(180deg, #1b2440 0%, var(--navy) 50%, #243457 100%);
  }
  .speaker-photo {
    position: absolute; left: 257px; top: 636px; width: 283px; height: 408px;
    background: linear-gradient(180deg, #8f857a 0%, #b0a594 40%, #c8512f 70%, #b8462a 100%);
  }
  .display { position: absolute; left: 0; top: 0; width: 807px; height: 1044px; pointer-events: none; }
  .display text { font-family: "Jost", sans-serif; }
  .title-word { filter: drop-shadow(3px 3px 3px rgba(0,0,0,.45)); }

  .label-speaker {
    position: absolute; left: 258px; top: 597px;
    font-weight: 700; font-size: 21px; letter-spacing: .5px; color: var(--navy-ink);
  }
  .speaker-name {
    position: absolute; left: 391px; top: 597px;
    font-weight: 400; font-size: 23px; letter-spacing: .3px; color: var(--paper);
  }
  .details {
    position: absolute; left: 568px; top: 643px; width: 235px;
    font-size: 16.5px; line-height: 22px; color: var(--paper);
  }
  .details .accent { color: var(--amber); font-weight: 700; }
  .venue { margin-bottom: 23px; font-style: normal; }
  .email { margin-top: 32px; font-size: 15.5px; }
  .phone { margin-top: 26px; font-weight: 700; font-size: 18px; }
</style>
</head>
<body>
<main class="flyer">
  <div class="panel panel--flame"></div>
  <div class="panel panel--brand">
    <span class="brand-dot"></span>
    <span class="brand-name">HALVERN</span>
  </div>
  <div class="panel panel--year"></div>
  <div class="panel panel--title"></div>
  <div class="panel panel--details"></div>

  <div class="speaker-photo" role="img" aria-label="Portrait photo of the speaker, Prophet Marcus Olunde, in an orange suit against a brick wall"></div>

  <svg class="display" viewBox="0 0 807 1044">
    <!-- focus words -->
    <text x="22" y="150" textLength="323" lengthAdjust="spacingAndGlyphs" font-size="178" font-weight="200" fill="#e38a3c" opacity=".85">FIRE</text>
    <text transform="translate(241,1006) rotate(-90)" x="0" y="0" textLength="834" lengthAdjust="spacingAndGlyphs" font-size="313" font-weight="100" fill="var(--blush)">REVIVAL</text>
    <text transform="translate(283,169) rotate(90)" x="0" y="0" textLength="421" lengthAdjust="spacingAndGlyphs" font-size="80" font-weight="800" fill="#3a2336" opacity=".5">PROPHETIC</text>
    <text transform="translate(786,197) rotate(-90)" x="0" y="0" textLength="172" lengthAdjust="spacingAndGlyphs" font-size="78" font-weight="400" fill="var(--amber)">2020</text>

    <!-- event title -->
    <text class="title-word" x="394" y="329" textLength="384" lengthAdjust="spacingAndGlyphs" font-size="104" font-weight="800" fill="var(--amber)">KESTREL</text>
    <text class="title-word" x="394" y="388" textLength="384" lengthAdjust="spacingAndGlyphs" font-size="62" font-weight="700" fill="var(--paper)">SUMMIT</text>

    <!-- theme -->
    <text x="391" y="557" font-size="86" font-weight="700" fill="var(--amber)" textLength="131" lengthAdjust="spacingAndGlyphs">Fire</text>
    <text x="472" y="509" font-size="58" font-weight="600" fill="var(--paper)" textLength="48" lengthAdjust="spacingAndGlyphs">in</text>
    <text x="540" y="565" font-size="134" font-weight="300" fill="var(--navy)" stroke="var(--amber)" stroke-width="2.5">&amp;</text>
    <text x="691" y="509" font-size="58" font-weight="600" fill="var(--paper)" textLength="72" lengthAdjust="spacingAndGlyphs">on</text>
    <text x="636" y="557" font-size="86" font-weight="200" fill="var(--paper)" textLength="125" lengthAdjust="spacingAndGlyphs">Fire</text>

    <!-- icons -->
    <g>
      <circle cx="540" cy="675" r="17" fill="var(--amber-deep)"/>
      <path d="M540 666 a6 6 0 0 1 6 6 c0 5 -6 12 -6 12 c0 0 -6 -7 -6 -12 a6 6 0 0 1 6 -6z" fill="var(--navy)"/>
      <circle cx="540" cy="672" r="2.2" fill="var(--amber-deep)"/>

      <circle cx="540" cy="945" r="17" fill="var(--amber-deep)"/>
      <g fill="none" stroke="var(--navy)" stroke-width="1.6">
        <circle cx="540" cy="945" r="9"/>
        <ellipse cx="540" cy="945" rx="4" ry="9"/>
        <line x1="531" y1="945" x2="549" y2="945"/>
        <line x1="532.5" y1="940" x2="547.5" y2="940"/>
        <line x1="532.5" y1="950" x2="547.5" y2="950"/>
      </g>

      <circle cx="540" cy="991" r="17" fill="var(--amber-deep)"/>
      <path d="M534 981 l4 0 l2 6 l-3 2 c1.5 3 3.5 5 6 6 l2 -3 l6 2 l0 4 c-1 1 -2 2 -4 2 c-8 -1 -14 -7 -15 -15 c0 -2 1 -3 2 -4z" fill="var(--navy)"/>
    </g>
  </svg>

  <p class="label-speaker">SPEAKER</p>
  <p class="speaker-name">PROPHET MARCUS OLUNDE</p>

  <section class="details">
    <address class="venue">
      <span class="accent">Harlow Community Center</span><br>
      239 Fennimore Street<br>
      Portland, ME 04117
    </address>
    <div class="schedule">
      <span class="accent">Thursday</span><br>
      December 31st @ 6:30PM<br>
      <span class="accent">Friday</span><br>
      January 1st @ 6:30PM<br>
      <span class="accent">Saturday</span><br>
      2nd @ 6:30PM<br>
      <span class="accent">Sunday</span><br>
      3rd @ 4:30PM
    </div>
    <p class="email accent">contact@brightmeadowfold.org</p>
    <p class="phone">207 583 2914</p>
  </section>
</main>
</body>
</html>
```